Pet Resort Website Layout Update for Current Website

Established Dog Daycare, Overnight Care, and Grooming facility in need of a new layout for our website. Our current site is: www.PawHavenLodge.example. We are in the process of re-branding and need a new website to pull our image together.

We are looking to update our look and feel to a more fun and personable layout without looking 'cute'.

The project calls for multiple pages to be created for our final website. However, we are not requiring you to submit all finished pages. To get a good feel for your style that you are presenting please design a home page and two others of your choosing so we may see what you have to offer. If your designs are selected, we will need to work with each other to create the remaining pages needed for the whole website. We are estimating the final product being 10-15 pages.

The new website will use most of our existing content. The home page will need navigation for 'Home', 'About Us', 'Services', 'Get Started', and 'Contact us'.

We like layouts similar to: www.tailwoodpines.example

We like the home page to have a slide show of photos, easy to find phone number, logo, with larger areas to click on for 'Dog Daycare' Overnight Care' Grooming'.

Home page should also have an area spotlighting our new client specials. Testimonials should be found throughout the site, or scrolling in an area on the home page.

Target Market(s)

Dog owners who think of their pets as a member of their family and not 'just a dog'. Families who work long hours or who travel a lot. Women walk through our door more than men. Various ages from 22-65+ . We target a higher income demographic.

Industry/Entity Type

Daycare

Colors
acd036
85cae6
fcfbe6

Requirements
Must have
• Must use the colors of green and blue as provided on the sample file of our business cards. I do not know the actual colors but matching as close as possible is fine with us.

Must be attractive, easy to navigate and find information without feeling overwhelming. Please see an example of at tailwoodpines.example on how we would like to use a photo slide show on the home page.

We will supply photo or stock photography for the final design when the website is put together.

Must be a wordpress design.
Nice to have
• Our final design pages will include:
Home: phone number, logo, slide show, new client offer, facebook tab, client testimonial scrolling or changing area, larger navigation tab for Daycare, Overnight Care and Grooming.

Again the final design chosen will require layouts for more pages. We welcome a design of the front page and two others so we can get a feel for your style before spending the time to create the required 10-15 pages for the final website.
Should not have
• Should not be cluttered with lots of 'noise'. Should not contain clip art. Please make it professional and not 'cute'.

```html
<!DOCTYPE html>
<html lang="en">
<head>
<meta charset="utf-8">
<title>Tailwag Manor — Home</title>
<link href="https://fonts.googleapis.com/css2?family=Open+Sans:ital,wght@0,400;0,600;0,700;1,600;1,700&display=swap" rel="stylesheet">
<style>
:root{
  --green:#acd036;
  --nav-green:#7c9a24;
  --blue:#85cae6;
  --cream:#fcfbe6;
  --cream-deep:#f6eeb4;
  --brown:#4a3d27;
  --brown-text:#4b3a22;
  --grey-text:#8a8370;
  --muted:#a7a7a7;
}
*{box-sizing:border-box;margin:0;padding:0}
html,body{width:1024px;height:1200px;overflow:hidden}
body{font-family:"Open Sans",Arial,sans-serif;background:#fff;position:relative;color:var(--brown-text)}
.abs{position:absolute}

/* header */
.site-header{position:absolute;left:0;top:0;width:1024px;height:80px;background:#fff}
.brand{position:absolute;left:157px;top:24px;display:flex;align-items:center;gap:8px}
.brand-mark{width:26px;height:26px;background:var(--blue)}
.brand-name{font-size:17px;font-weight:600;color:var(--brown);letter-spacing:.3px}
.phone-tab{position:absolute;left:679px;top:0;width:185px;height:24px;background:#fff;border-radius:0 0 4px 4px;box-shadow:0 1px 4px rgba(0,0,0,.18);display:flex;align-items:center;justify-content:center;gap:7px;font-size:11px;font-weight:700;color:var(--brown-text)}
.main-nav{position:absolute;top:32px;left:450px;display:flex;align-items:center;font-size:12px;font-weight:700;color:var(--nav-green)}
.main-nav a{color:inherit;text-decoration:none}
.nav-home{width:65px;height:28px;border-radius:3px;background:linear-gradient(#c0de55,#98bf25);color:#fff !important;display:flex;align-items:center;justify-content:center;box-shadow:0 1px 2px rgba(0,0,0,.25)}
.main-nav a:nth-child(2){margin-left:38px}
.main-nav a:nth-child(3){margin-left:41px}
.main-nav a:nth-child(4){margin-left:43px}
.main-nav a:nth-child(5){margin-left:35px}

/* hero */
.hero{position:absolute;left:0;top:80px;width:1024px;height:331px;background:radial-gradient(ellipse at 50% 25%,#f4fbfd 0%,#d8eff5 55%,#a8d8e6 100%)}
.slide{position:absolute;left:152px;top:16px;width:720px;height:282px;border-radius:6px;overflow:hidden;box-shadow:0 10px 16px -6px rgba(40,80,90,.35);background:linear-gradient(160deg,#5aa8dc 0%,#8cc4e2 45%,#8fbf6a 100%)}
.caption{position:absolute;left:18px;top:198px;width:368px;height:66px;background:rgba(74,55,30,.88);border-radius:4px;color:#fff;font-size:15px;line-height:20px;padding:13px 16px}
.arrow{position:absolute;top:126px}

/* services */
.services{position:absolute;left:0;top:411px;width:1024px;height:268px;background:linear-gradient(180deg,var(--cream-deep) 0%,#fbf8dc 35%,#fbf8dc 65%,var(--cream-deep) 100%)}
.card{position:absolute;top:26px;width:188px;height:88px;background:#fcfbf0;border:1px solid #ece8cc;border-radius:3px;box-shadow:0 1px 3px rgba(0,0,0,.08);text-align:center}
.card-icon{position:absolute;left:73px;top:10px;width:42px;height:42px}
.card h2{position:absolute;left:0;right:0;top:57px;font-size:16px;font-weight:700;color:var(--brown-text)}
.card-text{position:absolute;top:128px;width:190px;font-size:10.4px;line-height:14.4px;color:var(--grey-text)}
.read-more{position:absolute;top:201px;width:88px;height:31px;background:linear-gradient(#c3df5c,#9cc22b);border:1px solid #d9ec9c;box-shadow:0 1px 2px rgba(0,0,0,.2);color:#fff;font-size:10.5px;font-weight:700;display:flex;align-items:center;justify-content:center;text-shadow:0 1px 1px rgba(0,0,0,.25)}

/* testimonials */
.testimonials{position:absolute;left:0;top:679px;width:1024px;height:267px;background:#faf8e3}
.testimonials h2{position:absolute;left:0;right:0;top:25px;text-align:center;font-size:16px;font-weight:700;color:var(--brown-text)}
.person{position:absolute;top:68px;display:flex;gap:13px}
.avatar{width:40px;height:40px;background:linear-gradient(#e8c79a,#c79a6e)}
.avatar.alt{background:linear-gradient(#c9c2b8,#8d857a)}
.person-name{font-size:15px;color:var(--brown-text);line-height:18px;margin-top:-1px}
.person-role{font-size:10.5px;color:var(--muted);margin-top:3px}
.quote{position:absolute;top:125px;width:391px;height:86px;background:var(--blue);border-radius:3px;color:#fff;font-size:13px;font-style:italic;font-weight:600;line-height:19px;padding:14px 20px 0 33px;text-align:justify}
.quote::before{content:"";position:absolute;left:52px;top:-9px;border:9px solid transparent;border-top:0;border-bottom-color:var(--blue)}
.quote-mark{position:absolute;left:11px;top:13px;font-size:24px;font-style:normal;font-weight:700;line-height:22px}

/* footer */
.site-footer{position:absolute;left:0;top:946px;width:1024px;height:211px;background:#fff}
.footer-brand{position:absolute;left:112px;top:76px;display:flex;align-items:center;gap:12px}
.footer-brand .brand-mark{width:40px;height:40px}
.footer-brand .brand-name{font-size:28px;font-weight:600}
.col{position:absolute;top:38px;font-size:10.5px;color:var(--brown-text)}
.col h3{font-size:10.5px;font-weight:400;color:var(--grey-text);letter-spacing:.3px;margin-bottom:14px}
.col li{list-style:none;height:24.4px}
.contact{top:34px;left:592px}
.contact-row{display:flex;gap:12px;margin-bottom:11px;line-height:14px}
.contact-row svg{flex:none;margin-top:1px}
.map{position:absolute;left:758px;top:64px;width:155px;height:63px;background:linear-gradient(135deg,#e8e6df,#dcdad2 60%,#b9cfdc);border:1px solid #e2e0d8}
.to-top{position:absolute;left:875px;top:146px;width:38px;height:38px;border-radius:50%;background:var(--brown)}
.copyright{position:absolute;left:0;top:1157px;width:1024px;height:43px;background:var(--brown);color:#a39a86;font-size:10px;text-align:center;line-height:43px}
</style>
</head>
<body>

<header class="site-header">
  <div class="brand"><span class="brand-mark"></span><span class="brand-name">Tailwag Manor</span></div>
  <div class="phone-tab">
    <svg width="10" height="10" viewBox="0 0 24 24"><path fill="#4a3d27" d="M6.6 10.8a15 15 0 0 0 6.6 6.6l2.2-2.2c.3-.3.7-.4 1-.2 1.1.4 2.3.6 3.6.6.6 0 1 .4 1 1V20c0 .6-.4 1-1 1A17 17 0 0 1 3 4c0-.6.4-1 1-1h3.5c.6 0 1 .4 1 1 0 1.3.2 2.5.6 3.6.1.3 0 .7-.2 1z"/></svg>
    CALL US +1800.555.0142
  </div>
  <nav class="main-nav">
    <a class="nav-home" href="#">Home</a>
    <a href="#">About</a>
    <a href="#">Services</a>
    <a href="#">Get Started</a>
    <a href="#">Contact</a>
  </nav>
</header>

<section class="hero">
  <svg class="arrow" style="left:110px" width="22" height="30" viewBox="0 0 22 30"><path d="M17 3 5 15l12 12" fill="none" stroke="#acd036" stroke-width="5"/></svg>
  <div class="slide" role="img" aria-label="Slideshow photo: a smiling family relaxing on the lawn with their dog">
    <div class="caption">Lorem ipsum dolor sit amet consectetur adipiscing elit.</div>
  </div>
  <svg class="arrow" style="left:892px" width="22" height="30" viewBox="0 0 22 30"><path d="M5 3l12 12L5 27" fill="none" stroke="#acd036" stroke-width="5"/></svg>
</section>

<section class="services">
  <div class="card" style="left:112px">
    <svg class="card-icon" viewBox="0 0 42 42" aria-label="Daytime icon" role="img"><circle cx="21" cy="21" r="8" fill="#85cae6"/><g stroke="#85cae6" stroke-width="3" stroke-linecap="round"><path d="M21 3v6M21 33v6M3 21h6M33 21h6M8 8l4 4M30 30l4 4M34 8l-4 4M12 30l-4 4"/></g></svg>
    <h2>Dog Daycare</h2>
  </div>
  <div class="card" style="left:316px">
    <svg class="card-icon" viewBox="0 0 42 42" aria-label="Lodging icon" role="img"><path d="M4 20 21 6l17 14" fill="none" stroke="#85cae6" stroke-width="3.5" stroke-linejoin="round"/><path d="M9 19v19h24V19" fill="#85cae6"/><rect x="17" y="26" width="8" height="12" fill="#fcfbf0"/></svg>
    <h2>Overnight Care</h2>
  </div>
  <div class="card" style="left:520px">
    <svg class="card-icon" viewBox="0 0 42 42" aria-label="Scissors icon" role="img"><g fill="none" stroke="#85cae6" stroke-width="3.5" stroke-linecap="round"><circle cx="11" cy="31" r="5"/><circle cx="31" cy="31" r="5"/><path d="M14 27 32 5M28 27 10 5"/></g></svg>
    <h2>Grooming</h2>
  </div>
  <div class="card" style="left:724px">
    <svg class="card-icon" viewBox="0 0 42 42" aria-label="Award ribbon icon" role="img"><path d="M14 22 10 39l6-3 4 5 2-14M28 22l4 17-6-3-4 5-2-14" fill="#85cae6"/><circle cx="21" cy="15" r="11" fill="#85cae6"/><circle cx="21" cy="15" r="6" fill="none" stroke="#fcfbf0" stroke-width="2"/></svg>
    <h2>Client Specials</h2>
  </div>

  <p class="card-text abs" style="left:112px">Lorem ipsum dolor sit amet, consecte-tur adipisicing elit, sed do eiusmod tempor incididunt ut labore et dolore magna aliqua.</p>
  <p class="card-text abs" style="left:315px">Lorem ipsum dolor sit amet, consecte-tur adipisicing elit, sed do eiusmod tempor incididunt ut labore et dolore magna aliqua.</p>
  <p class="card-text abs" style="left:519px">Lorem ipsum dolor sit amet, consecte-tur adipisicing elit, sed do eiusmod tempor incididunt ut labore et dolore magna aliqua.</p>
  <p class="card-text abs" style="left:731px">Lorem ipsum dolor sit amet, consecte-tur adipisicing elit, sed do eiusmod tempor incididunt ut labore et dolore magna aliqua.</p>

  <a class="read-more" style="left:110px">Read More</a>
  <a class="read-more" style="left:316px">Read More</a>
  <a class="read-more" style="left:517px">Read More</a>
  <a class="read-more" style="left:723px">Read More</a>
</section>

<section class="testimonials">
  <h2>Client Testimonials</h2>
  <div class="person" style="left:112px">
    <div class="avatar" role="img" aria-label="Portrait of the client"></div>
    <div><div class="person-name">Mara Ellison</div><div class="person-role">Housewife</div></div>
  </div>
  <div class="person" style="left:521px">
    <div class="avatar alt" role="img" aria-label="Portrait of the client"></div>
    <div><div class="person-name">John Doe</div><div class="person-role">Businessman</div></div>
  </div>
  <blockquote class="quote" style="left:112px"><span class="quote-mark">&ldquo;</span>Lorem ipsum dolor sit amet, consectetur adipisicing elit, sed do eiusmod tempor incididunt ut labore et dolore magna aliqua.</blockquote>
  <blockquote class="quote" style="left:521px"><span class="quote-mark">&ldquo;</span>Lorem ipsum dolor sit amet, consectetur adipisicing elit, sed do eiusmod tempor incididunt ut labore et dolore magna aliqua.</blockquote>
</section>

<footer class="site-footer">
  <div class="footer-brand"><span class="brand-mark"></span><span class="brand-name">Tailwag Manor</span></div>
  <div class="col" style="left:376px">
    <h3>NAVIGATION</h3>
    <ul><li>Home</li><li>About</li><li>Services</li><li>Get Started</li><li>Contact</li></ul>
  </div>
  <div class="col" style="left:487px">
    <h3>SERVICES</h3>
    <ul><li>Dog Daycare</li><li>Overnight Care</li><li>Grooming</li><li>Client Specials</li></ul>
  </div>
  <div class="col contact">
    <h3>CONTACT US</h3>
    <div class="contact-row"><svg width="14" height="14" viewBox="0 0 24 24"><path fill="#8a8370" d="M6.6 10.8a15 15 0 0 0 6.6 6.6l2.2-2.2c.3-.3.7-.4 1-.2 1.1.4 2.3.6 3.6.6.6 0 1 .4 1 1V20c0 .6-.4 1-1 1A17 17 0 0 1 3 4c0-.6.4-1 1-1h3.5c.6 0 1 .4 1 1 0 1.3.2 2.5.6 3.6.1.3 0 .7-.2 1z"/></svg>+1800-555-0142</div>
    <div class="contact-row"><svg width="14" height="12" viewBox="0 0 14 12"><rect x="1" y="1" width="12" height="10" rx="1" fill="none" stroke="#8a8370" stroke-width="1.4"/><path d="M1 2l6 5 6-5" fill="none" stroke="#8a8370" stroke-width="1.4"/></svg>info@yourwebsite.com</div>
    <div class="contact-row"><svg width="14" height="16" viewBox="0 0 14 16"><path d="M7 1a5 5 0 0 0-5 5c0 4 5 9 5 9s5-5 5-9a5 5 0 0 0-5-5z" fill="#8a8370"/><circle cx="7" cy="6" r="2" fill="#fff"/></svg><span>Your Address,<br>Your Zip Code</span></div>
  </div>
  <div class="map" role="img" aria-label="Street map showing the resort location"></div>
  <a class="to-top" aria-label="Back to top"><svg width="38" height="38" viewBox="0 0 38 38"><path d="M13 21l6-6 6 6" fill="none" stroke="#acd036" stroke-width="3.5"/></svg></a>
</footer>

<div class="copyright">Copyright © 2014 TailwagManor.example. All rights reserved.</div>

</body>
</html>
```